Morevo - Augmented Reality Mobile application

We need a logo design for new mobile application. The overall objective of the application is to build a digital content delivery tool for scanning and recognizing of an image (marker) through a mobile application. The provision of digital content to the user takes place via augmeted reality and / or redirecting the user to a given digital content source.We don`t have any color scheme yet, but we have been thinking about something colorful. We are open for ideas.I have uploaded our working logos, but we are not strongly engaged with them.
Updates

Hello everybody, I have increased the budget of the project Regards

Target Market(s)

Entertainment; Education;

Industry/Entity Type

Entertainment

Logo Text

"Morevo" is the name of the product. We want a logo enough distinguishable to be recognized even without the text

Font styles to use
Serif
Sans Serif

Colors

Designer to choose colors to be used in the design.

Requirements
Must have
• We have attached a document with some information about the product. Feel free to use whatever found useful in it.
• We are not looking for the same design, rather an alternative one. We need all of the screens mentioned in the document
Nice to have
Should not have

```html
<!DOCTYPE html>
<html lang="en">
<head>
<meta charset="utf-8">
<title>Morevo – App Screens</title>
<link href="https://fonts.googleapis.com/css2?family=Rubik:wght@400;500;700&family=Roboto:wght@400;500&display=swap" rel="stylesheet">
<style>
  :root {
    --bg: #15144a;
    --screen-top: #4b4b96;
    --screen-bottom: #2e2d72;
    --grid-bg: #262561;
    --white: #ffffff;
    --muted: #c9c9ea;
    --accent: #16c8f0;
    --accent-dim: #1a9ab8;
    --button: #45458f;
  }
  * { box-sizing: border-box; margin: 0; padding: 0; }
  html, body { width: 1200px; height: 1200px; overflow: hidden; background: var(--bg); }
  body { position: relative; font-family: "Roboto", sans-serif; color: var(--white); }

  .brand { position: absolute; left: 112px; top: 216px; }
  .brand__emblem { width: 112px; height: 112px; border-radius: 50%; border: 4px solid var(--white); }
  .brand__name { font-family: "Rubik", sans-serif; font-weight: 700; font-size: 35px; letter-spacing: 0.5px; margin-top: 38px; line-height: 1; }
  .brand__slogan { font-family: "Rubik", sans-serif; font-size: 13px; margin-top: 8px; }

  .screen {
    position: absolute; width: 184px; height: 398px; border-radius: 26px; overflow: hidden;
    background: linear-gradient(180deg, var(--screen-top), var(--screen-bottom));
  }
  .screen > * { position: absolute; }
  .status { top: 9px; left: 0; right: 0; height: 8px; font-size: 6px; color: var(--muted); }
  .status__time { position: absolute; left: 18px; }
  .status__icons { position: absolute; right: 14px; top: 1px; display: flex; gap: 3px; }
  .status__icons i { display: block; width: 6px; height: 4px; background: var(--muted); border-radius: 1px; }
  .home-bar { bottom: 7px; left: 60px; width: 64px; height: 2px; background: var(--white); border-radius: 2px; opacity: .8; }

  .center { left: 0; right: 0; text-align: center; }
  .app-emblem { border-radius: 50%; border: 2px solid var(--white); }
  .app-name { font-family: "Rubik", sans-serif; font-weight: 700; font-size: 19px; }
  .app-slogan { font-family: "Rubik", sans-serif; font-size: 6.5px; }
  .copyright { font-size: 6.4px; }
  .title { font-family: "Rubik", sans-serif; font-size: 10.5px; }
  .lorem { left: 12px; right: 12px; text-align: center; font-size: 5.8px; line-height: 1.35; color: var(--muted); }

  .pager { left: 0; right: 0; display: flex; justify-content: center; gap: 4px; }
  .pager i { width: 5px; height: 5px; border-radius: 50%; border: 1px solid var(--white); }
  .pager i.on { background: var(--white); }
  .pager--splash i { border: 0; background: var(--accent); }
  .pager--splash i:last-child { background: var(--accent-dim); }

  .menu-btn {
    left: 14px; width: 152px; height: 41px; border-radius: 3px;
    background: linear-gradient(90deg, var(--button), rgba(69,69,143,0.4));
    display: flex; align-items: center; gap: 12px; padding-left: 12px;
    font-family: "Rubik", sans-serif; font-weight: 700; font-size: 10px;
  }

  .illus { border-radius: 3px; }

  .topbar { left: 10px; right: 10px; top: 36px; display: flex; align-items: center; justify-content: space-between; font-family: "Rubik", sans-serif; font-size: 10px; }
  .topbar__left { display: flex; align-items: center; gap: 3px; }
  .tabs { top: 62px; left: 0; right: 0; display: flex; font-size: 7px; color: var(--muted); }
  .tabs span { width: 62px; text-align: center; white-space: nowrap; }
  .tabs span.on { color: var(--white); }
  .tab-line { top: 75px; left: 12px; width: 56px; height: 2px; background: var(--white); }
  .grid-bg { top: 82px; left: 0; right: 0; bottom: 0; background: var(--grid-bg); }
  .tile { width: 50px; height: 62px; }
  .tile-label { font-size: 4.8px; color: var(--muted); }

  .camera { top: 58px; left: 0; right: 0; bottom: 0;
    background: linear-gradient(180deg, #2a2a2a 0%, #4a4a48 45%, #cfcfcc 72%, #e6e6e3 100%); }
  .vase { left: 46px; top: 120px; width: 90px; height: 178px; border-radius: 30px 30px 40px 40px;
    background: linear-gradient(90deg, #9b9b97, #d8d8d3 45%, #8a8a86); }
  .thumb { width: 38px; height: 38px; border-radius: 50%; background: var(--white); top: 343px; display: flex; align-items: center; justify-content: center; }
  .thumb b { width: 16px; height: 16px; border-radius: 50%; }

  .note { position: absolute; left: 658px; top: 556px; width: 200px; text-align: center; font-family: "Rubik", sans-serif; font-weight: 500; font-size: 13px; line-height: 1.25; }
  .flow { position: absolute; left: 0; top: 0; pointer-events: none; }
</style>
</head>
<body>

<div class="brand">
  <div class="brand__emblem"></div>
  <div class="brand__name">Morevo</div>
  <div class="brand__slogan">Your logo slogan</div>
</div>

<!-- Splash -->
<section class="screen" style="left:370px; top:124px;">
  <div class="status"><span class="status__time">9:41</span><span class="status__icons"><i></i><i></i><i></i></span></div>
  <div class="app-emblem" style="left:66px; top:142px; width:52px; height:52px;"></div>
  <div class="center app-name" style="top:216px;">Morevo</div>
  <div class="center app-slogan" style="top:241px;">Your logo slogan</div>
  <div class="pager pager--splash" style="top:303px;"><i></i><i></i><i></i></div>
  <div class="center copyright" style="top:365px;">© 2013-2018 Company All rights reserved.</div>
  <div class="home-bar"></div>
</section>

<!-- Main menu -->
<section class="screen" style="left:661px; top:124px;">
  <div class="status"><span class="status__time">9:41</span><span class="status__icons"><i></i><i></i><i></i></span></div>
  <svg style="left:154px; top:32px;" width="11" height="11" viewBox="0 0 11 11"><circle cx="5.5" cy="5.5" r="4.5" fill="none" stroke="#fff" stroke-width="1"/><path d="M3.5 7V5M5.5 7V3.5M7.5 7V4.5" stroke="#fff" stroke-width="1"/></svg>
  <div class="app-emblem" style="left:32px; top:80px; width:50px; height:50px;"></div>
  <div class="app-name" style="top:155px; left:31px;">Morevo</div>
  <div class="app-slogan" style="top:179px; left:31px;">Your logo slogan</div>
  <div class="menu-btn" style="top:227px;">
    <svg width="24" height="24" viewBox="0 0 24 24" fill="none" stroke="#fff" stroke-width="1"><path d="M2 7V2h5M17 2h5v5M22 17v5h-5M7 22H2v-5"/><path d="M12 7l5 3v5l-5 3-5-3v-5z M7 10l5 3 5-3 M12 13v5"/></svg>
    Scan
  </div>
  <div class="menu-btn" style="top:277px;">
    <svg width="24" height="24" viewBox="0 0 24 24" fill="none" stroke="#fff" stroke-width="1"><circle cx="14" cy="9" r="6"/><path d="M10 14v7h6v-3h3v-4M3 16h6v6H3z M5 18h2"/></svg>
    How to
  </div>
  <div class="center app-slogan" style="top:342px; font-size:7.5px;">Broden your reality</div>
  <div class="center copyright" style="top:364px;">© 2013-2018 Company All rights reserved.</div>
  <div class="home-bar"></div>
</section>

<!-- Onboarding 1 -->
<section class="screen" style="left:950px; top:124px;">
  <div class="status"><span class="status__time">9:41</span><span class="status__icons"><i></i><i></i><i></i></span></div>
  <div class="illus" role="img" aria-label="Illustration of a printed marker lying flat" style="left:10px; top:146px; width:164px; height:58px; background:linear-gradient(180deg,#3a3a86,#23a9d6 60%,#16c8f0);"></div>
  <div class="center title" style="top:229px;">Place your marker</div>
  <div class="lorem" style="top:252px;">Lorem ipsum dolor sit amet, consectetur adipiscing elit, sed do eiusmod tempor incididunt ut labore et dolore magna aliqua. Ut enim ad minim veniam</div>
  <div class="pager" style="top:363px;"><i class="on"></i><i></i><i></i></div>
  <div class="home-bar"></div>
</section>

<!-- Onboarding 2 -->
<section class="screen" style="left:81px; top:628px;">
  <div class="status"><span class="status__time">9:41</span><span class="status__icons"><i></i><i></i><i></i></span></div>
  <div class="illus" role="img" aria-label="Illustration of a hand holding a phone over a marker" style="left:45px; top:104px; width:82px; height:88px; background:linear-gradient(180deg,#ffffff 0%,#16c8f0 40%,#f0968f 70%,rgba(255,255,255,0.1));"></div>
  <div class="center title" style="top:229px;">Scan that marker</div>
  <div class="lorem" style="top:252px;">Lorem ipsum dolor sit amet, consectetur adipiscing elit, sed do eiusmod tempor incididunt ut labore et dolore magna aliqua. Ut enim ad minim veniam</div>
  <div class="pager" style="top:363px;"><i></i><i class="on"></i><i></i></div>
  <div class="home-bar"></div>
</section>

<!-- Onboarding 3 -->
<section class="screen" style="left:370px; top:628px;">
  <div class="status"><span class="status__time">9:41</span><span class="status__icons"><i></i><i></i><i></i></span></div>
  <div class="illus" role="img" aria-label="Illustration of a hand holding a phone showing a plant" style="left:45px; top:98px; width:82px; height:94px; background:linear-gradient(180deg,#ffffff 0%,#7ed04a 30%,#16c8f0 50%,#f0968f 72%,rgba(255,255,255,0.1));"></div>
  <div class="center title" style="top:229px;">Add to collections</div>
  <div class="lorem" style="top:252px;">Lorem ipsum dolor sit amet, consectetur adipiscing elit, sed do eiusmod tempor incididunt ut labore et dolore magna aliqua. Ut enim ad minim veniam</div>
  <div class="pager" style="top:363px;"><i></i><i></i><i class="on"></i></div>
  <div class="home-bar"></div>
</section>

<!-- Collections -->
<section class="screen" style="left:661px; top:628px;">
  <div class="status"><span class="status__time">9:41</span><span class="status__icons"><i></i><i></i><i></i></span></div>
  <div class="topbar">
    <span class="topbar__left">← Collections</span>
    <svg width="11" height="11" viewBox="0 0 11 11"><circle cx="5.5" cy="5.5" r="4.5" fill="none" stroke="#fff"/><path d="M5.5 5v3M5.5 3.2v.6" stroke="#fff"/></svg>
  </div>
  <div class="tabs"><span class="on">3d Objects</span><span>Games</span><span>Videos</span></div>
  <div class="tab-line"></div>
  <div class="grid-bg"></div>

  <div class="tile" role="img" aria-label="Dark abstract 3D render" style="left:8px; top:94px; background:linear-gradient(135deg,#111,#555 50%,#222);"></div>
  <div class="tile" role="img" aria-label="Landscape with sky" style="left:67px; top:94px; background:linear-gradient(180deg,#a9d8ee,#6f9fb0 60%,#3b5560);"></div>
  <div class="tile" role="img" aria-label="Colourful grid pattern" style="left:127px; top:94px; background:linear-gradient(135deg,#e7eef3,#b6c3d2 50%,#d9a7ad);"></div>
  <div class="tile-label" style="left:8px; top:159px;">Object Name.3d</div>
  <div class="tile-label" style="left:67px; top:159px;">Object Name.3d</div>
  <div class="tile-label" style="left:127px; top:159px;">Object Name.3d</div>

  <div class="tile" role="img" aria-label="White 3D sculpture" style="left:8px; top:175px; background:linear-gradient(135deg,#6b4f4a,#d9d0cc 55%,#8f7873);"></div>
  <div class="tile" role="img" aria-label="Object on a wooden table" style="left:67px; top:175px; background:linear-gradient(180deg,#e0e0dc,#c8c2b6 60%,#b08656);"></div>
  <div class="tile" role="img" aria-label="Curved white object" style="left:127px; top:175px; background:linear-gradient(135deg,#ffffff,#ece8e1 60%,#c9b89a);"></div>
  <div class="tile-label" style="left:8px; top:240px;">Object Name.3d</div>
  <div class="tile-label" style="left:67px; top:240px;">Object Name.3d</div>
  <div class="tile-label" style="left:127px; top:240px;">Object Name.3d</div>

  <div class="tile" role="img" aria-label="Dark abstract 3D render" style="left:8px; top:256px; background:linear-gradient(135deg,#111,#555 50%,#222);"></div>
  <div class="tile" role="img" aria-label="Landscape with sky" style="left:67px; top:256px; background:linear-gradient(180deg,#a9d8ee,#6f9fb0 60%,#3b5560);"></div>
  <div class="tile" role="img" aria-label="Colourful grid pattern" style="left:127px; top:256px; background:linear-gradient(135deg,#e7eef3,#b6c3d2 50%,#d9a7ad);"></div>
  <div class="tile-label" style="left:8px; top:321px;">Object Name.3d</div>
  <div class="tile-label" style="left:67px; top:321px;">Object Name.3d</div>
  <div class="tile-label" style="left:127px; top:321px;">Object Name.3d</div>

  <div class="tile" role="img" aria-label="White 3D sculpture" style="left:8px; top:337px; background:linear-gradient(135deg,#6b4f4a,#d9d0cc 55%,#8f7873);"></div>
  <div class="tile" role="img" aria-label="Object on a wooden table" style="left:67px; top:337px; background:linear-gradient(180deg,#e0e0dc,#c8c2b6 60%,#b08656);"></div>
  <div class="tile" role="img" aria-label="Curved white object" style="left:127px; top:337px; background:linear-gradient(135deg,#ffffff,#ece8e1 60%,#c9b89a);"></div>
  <div class="home-bar"></div>
</section>

<!-- Scan -->
<section class="screen" style="left:950px; top:628px;">
  <div class="status"><span class="status__time">9:41</span><span class="status__icons"><i></i><i></i><i></i></span></div>
  <div class="topbar">
    <span class="topbar__left">← Scan</span>
    <span style="display:flex; gap:10px; align-items:center;">
      <svg width="7" height="11" viewBox="0 0 7 11"><path d="M4.5 0L0 6.5h3L2 11l5-6.5H4z" fill="#fff"/></svg>
      <svg width="11" height="11" viewBox="0 0 11 11"><circle cx="5.5" cy="5.5" r="4.5" fill="none" stroke="#fff"/><path d="M5.5 5v3M5.5 3.2v.6" stroke="#fff"/></svg>
    </span>
  </div>
  <div class="camera" role="img" aria-label="Camera view of a ceramic vase on a table"></div>
  <div class="vase" role="img" aria-label="Ceramic vase"></div>
  <div class="center title" style="top:77px; font-weight:500; font-size:10px;">Scan your Marker</div>
  <svg style="left:16px; top:302px;" width="152" height="18" viewBox="0 0 152 18"><path d="M2 17V6M2 15h26" stroke="#111" stroke-width="4" fill="none"/><path d="M124 15h26M150 17V8" stroke="#111" stroke-width="4" fill="none"/></svg>
  <div class="thumb" style="left:13px;"><b style="background:#e4184a;"></b></div>
  <div class="thumb" style="left:60px;"><b style="background:#9ccf5a;"></b></div>
  <div class="thumb" style="left:107px; background:#2b2b2b;"><b style="background:#6f9a3a; width:22px; height:22px;"></b></div>
  <div class="thumb" style="left:155px;"><b style="background:#d8d2b8;"></b></div>
  <div class="home-bar"></div>
</section>

<div class="note">You can add more<br>navigation here</div>

<svg class="flow" width="1200" height="1200" viewBox="0 0 1200 1200" fill="none" stroke="rgba(255,255,255,0.75)" stroke-width="1" stroke-dasharray="4 3">
  <path d="M815 162 C 740 180, 640 240, 615 340 C 595 430, 640 560, 668 640"/>
  <path d="M855 262 C 900 240, 950 290, 985 340"/>
  <path d="M815 372 C 870 380, 905 430, 910 540 C 914 610, 925 650, 940 672"/>
  <path d="M782 606 V 690"/>
</svg>

</body>
</html>
```